Business Card Design Project

We require a business card template to cover basic contact information - our company logo, names of employees, title, mobile and email.

Target Market(s)

Corporate

Industry/Entity Type

Business

Font styles to use
Sans Serif

Requirements
Nice to have
• Thinking it would be great just to have the logo taking up approximately half the space (so it goes as far across the top of the card as possible) and then contact details in the lower half of the card. Keen just to use only the two colours in the logo, on a white background.
Should not have
• No fussy drawings

```html
<!DOCTYPE html>
<html lang="en">
<head>
<meta charset="utf-8">
<title>Tidewell Developments – Business Card</title>
<link rel="stylesheet" href="https://fonts.googleapis.com/css2?family=Open+Sans:wght@400;600&display=swap">
<style>
  :root {
    --stage: #e9e9e9;
    --card: #f2f2f2;
    --band: #2e7f9a;
    --brand-teal: #2a98a6;
    --text-light: #ffffff;
    --divider: rgba(255, 255, 255, 0.18);
  }
  * { margin: 0; padding: 0; box-sizing: border-box; }
  html, body {
    width: 1200px;
    height: 800px;
    overflow: hidden;
    background: var(--stage);
    font-family: "Open Sans", Arial, sans-serif;
  }
  .stage {
    width: 1200px;
    height: 800px;
    display: flex;
    align-items: center;
    justify-content: center;
  }
  .business-card {
    position: relative;
    width: 840px;
    height: 480px;
    background: var(--card);
    overflow: hidden;
    box-shadow: 0 10px 30px rgba(0, 0, 0, 0.12);
  }
  .wordmark {
    position: absolute;
    left: 62px;
    top: 58px;
    width: 716px;
    color: var(--brand-teal);
    font-weight: 600;
    line-height: 1;
  }
  .wordmark-name {
    display: block;
    font-size: 148px;
    letter-spacing: -4px;
  }
  .wordmark-tagline {
    display: block;
    text-align: right;
    font-size: 38px;
    margin-top: -6px;
    letter-spacing: 0.5px;
  }
  .contact-band {
    position: absolute;
    left: 0;
    right: 0;
    bottom: 0;
    height: 176px;
    background: var(--band);
    color: var(--text-light);
  }
  .band-divider {
    position: absolute;
    left: 430px;
    top: 24px;
    width: 1px;
    height: 128px;
    background: var(--divider);
    transform: rotate(18deg);
  }
  .person {
    position: absolute;
    left: 80px;
    bottom: 44px;
  }
  .person-name {
    font-size: 28px;
    font-weight: 600;
    line-height: 1.1;
  }
  .person-title {
    font-size: 16px;
    font-weight: 600;
    margin-top: 2px;
  }
  .contact-list {
    position: absolute;
    right: 52px;
    top: 30px;
    list-style: none;
    text-align: right;
    font-size: 18px;
    line-height: 32px;
  }
  .contact-list li {
    display: flex;
    align-items: center;
    justify-content: flex-end;
    gap: 12px;
  }
  .contact-icon {
    width: 16px;
    height: 16px;
    flex: none;
  }
</style>
</head>
<body>
<main class="stage">
  <article class="business-card">
    <h1 class="wordmark">
      <span class="wordmark-name">Tidewell</span>
      <span class="wordmark-tagline">developments</span>
    </h1>

    <section class="contact-band">
      <span class="band-divider"></span>

      <div class="person">
        <p class="person-name">Alex Morgan</p>
        <p class="person-title">Manager</p>
      </div>

      <ul class="contact-list">
        <li>
          <span class="contact-phone">0123 456 789</span>
          <svg class="contact-icon" viewBox="0 0 16 16" aria-hidden="true">
            <rect x="4" y="1" width="8" height="14" rx="1.5" fill="none" stroke="#fff" stroke-width="1.4"/>
            <line x1="7" y1="12.5" x2="9" y2="12.5" stroke="#fff" stroke-width="1.4"/>
          </svg>
        </li>
        <li>
          <span class="contact-email">alex.morgan@example.com</span>
          <svg class="contact-icon" viewBox="0 0 16 16" aria-hidden="true">
            <rect x="1" y="3.5" width="14" height="9" fill="#fff"/>
            <polyline points="1,3.5 8,9 15,3.5" fill="none" stroke="#2e7f9a" stroke-width="1.2"/>
          </svg>
        </li>
      </ul>
    </section>
  </article>
</main>
</body>
</html>
```